Harbor Ridge Holdings, LLC Business Card Design/Real Estate and Asset Mgmt.

Design business card with designer recommended colors using existing logo...teal color not mandatory. Business purpose is Asset Management and Real Estate.

The following text somewhere on the card:

HARBOR RIDGE HOLDINGS, LLC (llc can be very small font if needed.)
Tobias Welk GRI, RRP, CHA, CHME (the abbreviations can be a smaller font)
PROPLICENSEE
517 Fenwick Lane #204-31
Linden Falls, VT 05999
Toll Free: 888-555-0172
Cell: 555.555.0148
Email: tobiasrwelk@mailpost.example
www.harborridgeholdings.example

Target Market(s)

High net worth buyers and sellers. Will be providing commercial real estate sales and management services to banks and lenders who foreclose on bad debt collateral.

Industry/Entity Type

Real Estate

Contact Information for Business Card

Professional look. Maximum of two colors. Example: Logo one color and the text another. Or any combination the designer feels is appropriate.

Font styles to use
Other font styles liked:
• Designer's choice

Requirements
Must have
• Logo somewhere on the card.
Nice to have
• The card can be one sided or two sided or odd sized if the designer prefers.
• PROPLICENSEE Logo (small at the bottom or somewhere on the card. Even the back.)
Should not have
• Card should not be a folded card.

```html
<!DOCTYPE html>
<html lang="en">
<head>
<meta charset="UTF-8">
<title>Harbor Ridge Holdings, LLC — Business Card</title>
<link href="https://fonts.googleapis.com/css2?family=Arimo:wght@400;700&family=Montserrat:wght@600;700&display=swap" rel="stylesheet">
<style>
  :root {
    --page-bg: #e9eaeb;
    --card-white: #ffffff;
    --band-grey: #616264;
    --teal: #2fb6c1;
    --teal-deep: #20a7b3;
    --logo-grey: #5a5b5d;
    --text-white: #ffffff;
  }
  * { box-sizing: border-box; margin: 0; padding: 0; }
  html, body {
    width: 1200px; height: 800px; overflow: hidden;
    background: var(--page-bg);
    font-family: "Arimo", Arial, sans-serif;
  }
  .canvas {
    width: 1200px; height: 800px;
    display: flex; align-items: center; justify-content: center; gap: 40px;
  }
  .card {
    position: relative;
    width: 540px; height: 308px;
    background: var(--card-white);
    box-shadow: 0 10px 28px rgba(0,0,0,0.14);
    overflow: hidden;
  }

  /* Brand lockup */
  .brand {
    position: absolute; left: 0; right: 0;
    display: flex; flex-direction: column; align-items: center;
  }
  .brand-row { display: flex; align-items: center; gap: 10px; }
  .brand-square {
    width: 26px; height: 26px; background: var(--teal);
  }
  .brand-name {
    font-family: "Arimo", Arial, sans-serif;
    font-weight: 400; font-size: 19px; letter-spacing: 1.5px;
    color: var(--logo-grey); text-transform: uppercase; white-space: nowrap;
  }
  .brand-url {
    margin-top: 4px;
    font-size: 11px; letter-spacing: 0.6px; color: var(--logo-grey);
  }

  /* Back */
  .card-back .brand { top: 104px; }
  .card-back .url-band {
    position: absolute; left: 0; right: 0; top: 214px; height: 44px;
    background: var(--band-grey);
    display: flex; align-items: center; justify-content: center;
    color: var(--text-white); font-size: 15px; letter-spacing: 0.6px;
  }

  /* Front */
  .card-front .brand { top: 62px; }
  .name-band {
    position: absolute; left: 0; right: 0; top: 160px; height: 42px;
    background: var(--band-grey);
    display: flex; align-items: baseline; padding: 10px 0 0 34px; gap: 7px;
    color: var(--text-white);
  }
  .person-name {
    font-family: "Montserrat", Arial, sans-serif;
    font-weight: 700; font-size: 20px;
  }
  .credentials {
    font-family: "Montserrat", Arial, sans-serif;
    font-weight: 600; font-size: 12px; letter-spacing: 0.2px;
  }
  .contact-panel {
    position: absolute; left: 0; right: 0; top: 202px; bottom: 0;
    background: linear-gradient(120deg, var(--teal-deep), var(--teal) 55%, var(--teal-deep));
    display: flex; align-items: center; color: var(--text-white);
    font-size: 13px; line-height: 1.55;
  }
  .address {
    width: 268px; text-align: center;
  }
  .divider {
    width: 1px; height: 70px; background: rgba(255,255,255,0.85);
  }
  .direct-lines { padding-left: 22px; }
</style>
</head>
<body>
<main class="canvas">

  <section class="card card-back" aria-label="Card back">
    <div class="brand">
      <div class="brand-row">
        <span class="brand-square"></span>
        <span class="brand-name">Harbor Ridge Holdings, LLC</span>
      </div>
      <span class="brand-url">harborridgeholdings.example</span>
    </div>
    <div class="url-band">www.harborridgeholdings.example</div>
  </section>

  <section class="card card-front" aria-label="Card front">
    <div class="brand">
      <div class="brand-row">
        <span class="brand-square"></span>
        <span class="brand-name">Harbor Ridge Holdings, LLC</span>
      </div>
      <span class="brand-url">harborridgeholdings.example</span>
    </div>
    <div class="name-band">
      <span class="person-name">Tobias Welk</span>
      <span class="credentials">GRI, RRP, CHA, CHME (PROPLICENSEE)</span>
    </div>
    <div class="contact-panel">
      <div class="address">
        517 Fenwick Lane #204-31<br>
        Linden Falls, VT 05999<br>
        www.harborridgeholdings.example
      </div>
      <span class="divider"></span>
      <div class="direct-lines">
        Toll Free: 888-555-0172<br>
        Cell: 555.555.0148<br>
        Email: tobiasrwelk@mailpost.example
      </div>
    </div>
  </section>

</main>
</body>
</html>
```